Flyer / Small Safety "Poster" (A4 or 8.5x11" paper)

We're looking to create a series of safety signs for woodworkers to print on home printers using standard sized paper (A4 or 8.5x11" depending on where they are), or possibly to have printed on 17x22" paper.
Currently we want only the first one, but keep in mind that all should work together.
They need: Simple graphic. Bold Text. Company logo. Use company colors (orange, black, white.)
To begin, we will start with a single sign for hearing protection. Graphic or clip art to portray either ear plugs or ear-muff design. Text to say, "Hearing Protection is a Sound Investment."

Target Market(s)

USA Woodworkers & CNC Machinists - Male, 20-65 years old

Font styles to use
Sans Serif

Colors
f37122

Requirements
Must have
• Client logo
Nice to have
• Use client colors of black, white, & orange

```html
<!DOCTYPE html>
<html lang="en">
<head>
<meta charset="utf-8">
<title>Hearing Protection Safety Sign</title>
<link href="https://fonts.googleapis.com/css2?family=Anton&family=Montserrat:ital,wght@0,700;0,800;1,500&display=swap" rel="stylesheet">
<style>
  :root {
    --orange: #e07f32;
    --black: #111111;
    --charcoal: #4a4247;
    --paper: #f6f6f6;
    --backdrop: #d9d9da;
  }
  * { margin: 0; padding: 0; box-sizing: border-box; }
  html, body {
    width: 1130px; height: 1200px; overflow: hidden;
    background: var(--backdrop);
  }
  .sign {
    position: absolute; left: 142px; top: 0;
    width: 846px; height: 1200px;
    background: var(--paper);
    font-family: "Montserrat", Arial, sans-serif;
  }
  .earmuff-art {
    position: absolute; left: 32px; top: 117px;
    width: 774px; height: 733px;
    border-radius: 380px 380px 120px 120px;
    background:
      radial-gradient(ellipse at 8% 70%, rgba(232,148,58,.55), transparent 45%),
      radial-gradient(ellipse at 92% 70%, rgba(232,148,58,.55), transparent 45%),
      radial-gradient(ellipse at 50% 0%, rgba(74,66,71,.35), transparent 55%),
      linear-gradient(#f6f6f6, #ececec);
  }
  .headline {
    position: absolute; left: 0; width: 100%;
    text-align: center;
    font-family: "Anton", "Arial Narrow", sans-serif;
    font-weight: 400;
    text-transform: uppercase;
    transform-origin: 50% 0;
  }
  .headline--hearing {
    top: 262px; font-size: 212px; line-height: 212px;
    color: var(--orange); transform: scaleX(0.68);
  }
  .headline--protection {
    top: 474px; font-size: 106px; line-height: 106px;
    color: var(--black); transform: scaleX(0.95);
  }
  .subline {
    position: absolute; left: 0; width: 100%; text-align: center;
    font-weight: 700; line-height: 1;
  }
  .subline--sound { top: 604px; font-size: 58px; color: var(--black); }
  .subline--investment { top: 670px; font-size: 49px; color: var(--orange); }
  .brand {
    position: absolute; left: 0; top: 955px; width: 100%;
    display: flex; justify-content: center; align-items: center; gap: 14px;
  }
  .brand__mark { width: 46px; height: 46px; background: var(--black); }
  .brand__name { font-weight: 800; font-size: 44px; color: var(--black); letter-spacing: 1px; }
  .tagline {
    position: absolute; left: 0; top: 1040px; width: 100%; text-align: center;
    font-size: 16px; font-weight: 500; font-style: italic; color: var(--charcoal);
  }
  .web {
    position: absolute; left: 0; top: 1108px; width: 100%; text-align: center;
    font-size: 34px; font-weight: 800; letter-spacing: 2px; color: var(--black);
  }
  .web span { color: var(--orange); }
  .bottom-band {
    position: absolute; left: 0; bottom: 4px; width: 100%; height: 8px;
    background: var(--orange);
  }
</style>
</head>
<body>
  <main class="sign">
    <div class="earmuff-art" role="img" aria-label="Illustration of orange and charcoal safety earmuffs with headband arching over the headline"></div>
    <h1 class="headline headline--hearing">Hearing</h1>
    <h2 class="headline headline--protection">Protection</h2>
    <p class="subline subline--sound">Is a Sound</p>
    <p class="subline subline--investment">INVESTMENT</p>
    <div class="brand">
      <span class="brand__mark"></span>
      <span class="brand__name">EDGELINE SUPPLY</span>
    </div>
    <p class="tagline">Sharp bits for every shop and every build</p>
    <p class="web">www.<span>edgelinesupply</span>.com</p>
    <div class="bottom-band"></div>
  </main>
</body>
</html>
```